Gather the Orchard Gala Graphic Design

I’m seeking a professional graphic designer experienced in event branding to create a cohesive suite of materials for our third annual fundraising gala, “Gather the Orchard.” This year's theme is " An Evening in Linen to Gather the Orchard" Need to design collateral for website, social media and email blasts.
Target Market(s)
Affluent gala attendees
Industry/Entity Type
Fundraising / Charity / Outdoors / Sports
Font styles to use
Decorative
Script
Colors
0054AA
0677BA
7BADD7
CADEEF
E8F1F8
0094D4
00A9DD
6FCCEA
C7EBF8
E9F6FB
00AB8E
00BBA5
67D7C9
C6EFE9
E9F9F6
6B429C
8869AF
B7A5CE
E3DAEB
F3F0F8

```html
<!DOCTYPE html>
<html lang="en">
<head>
<meta charset="utf-8">
<title>Gather the Orchard Gala – Email Blast</title>
<link rel="stylesheet" href="https://fonts.googleapis.com/css2?family=Oswald:wght@200;300;400;500;600&family=Cinzel:wght@400;600&family=Montserrat:wght@400;600;700&display=swap">
<style>
  :root {
    --page: #ffffff;
    --ink: #1b1b1b;
    --navy-deep: #06111f;
    --navy: #0b1d33;
    --navy-mid: #10294a;
    --glow: #0094D4;
    --glow-soft: #6FCCEA;
    --ice: #C7EBF8;
    --mist: #E9F6FB;
    --white: #ffffff;
    --silver-hi: #f4f6f8;
    --silver-lo: #9aa3ad;
    --rule: rgba(199, 235, 248, 0.55);
  }
  * { margin: 0; padding: 0; box-sizing: border-box; }
  html, body { width: 729px; height: 1200px; overflow: hidden; background: var(--page); }
  body { position: relative; font-family: "Montserrat", sans-serif; }

  .section-label {
    position: absolute; top: 30px; left: 0; width: 729px;
    text-align: center; font: 600 22px "Montserrat", sans-serif;
    letter-spacing: 1px; color: var(--ink);
  }

  .email-card {
    position: absolute; left: 73px; top: 110px; width: 583px; height: 1082px;
    background: linear-gradient(180deg, var(--navy-deep) 0%, var(--navy) 45%, var(--navy-deep) 100%);
    overflow: hidden; color: var(--white); text-align: center;
  }
  .frame-line { position: absolute; background: var(--rule); }

  .light-glow {
    position: absolute; left: 0; top: 150px; width: 583px; height: 380px;
    background: radial-gradient(ellipse 55% 50% at 50% 45%, rgba(111,204,234,0.7) 0%, rgba(0,148,212,0.4) 35%, rgba(0,84,170,0.12) 70%, rgba(0,84,170,0) 100%);
  }

  .invite-kicker {
    position: absolute; top: 44px; width: 100%;
    font: 300 20px "Oswald", sans-serif; letter-spacing: 4px; color: var(--mist);
  }
  .theme-line {
    position: absolute; top: 80px; width: 100%;
    font: 300 52px/1 "Oswald", sans-serif; letter-spacing: 1px; color: var(--white);
  }
  .theme-line small { font-size: 30px; letter-spacing: 1px; }

  .gala-title {
    position: absolute; top: 210px; width: 100%;
    font-family: "Oswald", sans-serif; font-weight: 500; color: var(--white);
    text-shadow: 0 0 18px rgba(111,204,234,0.7), 0 2px 0 rgba(0,0,0,0.35);
  }
  .gala-title .word-top { display: block; font-size: 108px; line-height: 1; letter-spacing: 1px; }
  .gala-title .word-bottom { display: block; margin-top: 4px; font-size: 96px; line-height: 1; }
  .gala-title .the { font-size: 26px; font-weight: 400; vertical-align: 48px; margin-right: 6px; }

  .gala-type {
    position: absolute; top: 448px; width: 100%;
    font: 400 24px "Cinzel", serif; letter-spacing: 1px; color: var(--white);
  }
  .celebration {
    position: absolute; top: 490px; width: 100%;
    font: 400 15px/25px "Cinzel", serif; color: var(--mist);
  }

  .magic-lead {
    position: absolute; top: 582px; width: 100%;
    font: 400 15px "Cinzel", serif; color: var(--mist);
  }
  .vip-title {
    position: absolute; top: 604px; width: 100%;
    font: 400 44px/1 "Oswald", sans-serif; letter-spacing: 1px; color: var(--white);
  }
  .vip-pitch {
    position: absolute; top: 660px; width: 100%;
    font: 400 14px/24px "Cinzel", serif; color: var(--mist);
  }

  .ticket-band {
    position: absolute; left: 0; top: 728px; width: 100%; height: 54px;
    background: linear-gradient(90deg, var(--silver-lo) 0%, var(--silver-hi) 30%, var(--white) 50%, var(--silver-hi) 70%, var(--silver-lo) 100%);
    color: var(--navy); font: 600 30px/54px "Oswald", sans-serif; letter-spacing: 1px;
  }

  .perk-grid {
    position: absolute; left: 36px; top: 808px; width: 511px;
    display: grid; grid-template-columns: repeat(4, 1fr); row-gap: 26px; list-style: none;
  }
  .perk { font: 600 11px/1.5 "Montserrat", sans-serif; color: var(--ice); text-transform: uppercase; }

  .event-details {
    position: absolute; left: 0; top: 918px; width: 100%; height: 96px;
  }
  .event-date { position: absolute; left: 20px; top: 8px; width: 110px; text-align: center; }
  .event-date .day { display: block; font: 500 50px/1 "Oswald", sans-serif; color: var(--white); }
  .event-date .month { display: block; margin-top: 4px; font: 400 11px "Montserrat", sans-serif; letter-spacing: 1px; color: var(--ice); }
  .detail-list { position: absolute; left: 156px; top: 8px; list-style: none; text-align: left; }
  .detail-list li {
    display: flex; align-items: center; gap: 9px; height: 26px; white-space: nowrap;
    font: 600 11px "Montserrat", sans-serif; color: var(--white); text-transform: uppercase;
  }
  .detail-list svg { width: 13px; height: 13px; flex: none; }

  .web-band {
    position: absolute; left: 0; top: 1030px; width: 100%; height: 52px;
    background: linear-gradient(90deg, var(--navy-mid), #1b3e66 50%, var(--navy-mid));
    font: 600 20px/52px "Montserrat", sans-serif; color: var(--white);
  }
</style>
</head>
<body>
  <div class="section-label">EMAIL BLASTS</div>

  <main class="email-card">
    <div class="frame-line" style="left:30px;top:30px;width:523px;height:1px"></div>
    <div class="frame-line" style="left:30px;top:30px;width:1px;height:180px"></div>
    <div class="frame-line" style="left:552px;top:30px;width:1px;height:180px"></div>
    <div class="frame-line" style="left:60px;top:148px;width:463px;height:1px"></div>
    <div class="frame-line" style="left:60px;top:160px;width:463px;height:1px;opacity:.5"></div>

    <div class="light-glow" role="img" aria-label="Soft blue beam of light glowing behind the gala title"></div>

    <p class="invite-kicker">YOU ARE INVITED TO</p>
    <h2 class="theme-line">AN EVENING <small>IN</small> LINEN</h2>

    <h1 class="gala-title">
      <span class="word-top">GATHER</span>
      <span class="word-bottom"><span class="the">THE</span>ORCHARD</span>
    </h1>

    <p class="gala-type">A FUNDRAISING GALA</p>
    <p class="celebration">IN CELEBRATION OF THE 150TH ANNIVERSARY<br>OF HARROW HILL ORCHARD</p>

    <div class="frame-line" style="left:120px;top:560px;width:343px;height:1px"></div>

    <p class="magic-lead">REIGNITE THE MAGIC WITH AN EXCLUSIVE</p>
    <h3 class="vip-title">VIP PACKAGE</h3>
    <p class="vip-pitch">YOUR GOLDEN TICKET TO A REMARKABLE<br>NIGHT OF GLAMOUR AND PHILANTHROPY</p>

    <div class="ticket-band">GET YOUR TICKETS TODAY!</div>

    <ul class="perk-grid">
      <li class="perk">VIP Pre Gala<br>Experience</li>
      <li class="perk">Delicious<br>Dinner for 10</li>
      <li class="perk">Unlimited<br>Premium Bar</li>
      <li class="perk">Exclusive Meet<br>&amp; Greet</li>
      <li class="perk">Dedicated<br>Wine Service</li>
      <li class="perk">Bottle of<br>Wine Souvenir</li>
      <li class="perk">Custom Art<br>Keepsake</li>
      <li class="perk">Prime Table<br>Placement</li>
    </ul>

    <div class="frame-line" style="left:30px;top:910px;width:523px;height:1px"></div>

    <section class="event-details">
      <div class="event-date">
        <span class="day">18TH</span>
        <span class="month">NOVEMBER 2025</span>
      </div>
      <div class="frame-line" style="left:140px;top:6px;width:1px;height:80px"></div>
      <ul class="detail-list">
        <li>
          <svg viewBox="0 0 14 14"><circle cx="7" cy="7" r="6" fill="none" stroke="#fff" stroke-width="1.5"/><path d="M7 3.5V7l2.5 1.5" fill="none" stroke="#fff" stroke-width="1.5"/></svg>
          Cocktails 6-PM VIP Ticket Holders 5:00PM
        </li>
        <li>
          <svg viewBox="0 0 14 14"><path d="M7 13S2 8 2 5a5 5 0 0 1 10 0c0 3-5 8-5 8z" fill="#fff"/><circle cx="7" cy="5" r="1.8" fill="#0b1d33"/></svg>
          Cedar Point Key - 41820 Shoreline Hwy - Brookhaven
        </li>
        <li>
          <svg viewBox="0 0 14 14"><path d="M7 1l1.8 3.8 4.2.5-3.1 2.9.8 4.1L7 10.3 3.3 12.3l.8-4.1L1 5.3l4.2-.5z" fill="#fff"/></svg>
          Cocktail Attire - Space is Limited
        </li>
      </ul>
    </section>

    <div class="web-band">@www.saveharrowhillorchard.org</div>
  </main>
</body>
</html>
```